Velmar Industrial Coatings

We are looking to improve our business cards. Our company installs industrial floor and wall coatings in industrial, chemical and food processing plants.
Our coatings which consist of epoxy, urethane, and vinyl esters provide chemical and abrasion resistant surface with non-skid properties that are easy to clean.

Target Market(s)

food manufacturing, chemical plants, breweries and wineries, warehouses, clean room floors.

Industry/Entity Type

Construction

Contact Information for Business Card

improved current logo.

Colors

Designer to choose colors to be used in the design.

Requirements
Must have
• the information from uploaded file
Nice to have
• "We'll be outstanding on your floors."

```html
<!DOCTYPE html>
<html lang="en">
<head>
<meta charset="utf-8">
<title>Velmar Industrial Coatings — Business Cards</title>
<link rel="stylesheet" href="https://fonts.googleapis.com/css2?family=Open+Sans:wght@400;600;700&display=swap">
<style>
  :root {
    --backdrop: #2c3238;
    --card: #cdbfb7;
    --ink-brown: #2e1a14;
    --ink-body: #3a302c;
    --ink-muted: #5a4f4a;
    --green: #2f8a3a;
    --green-line: #3c8f45;
  }
  * { box-sizing: border-box; margin: 0; padding: 0; }
  html, body {
    width: 1200px; height: 900px; overflow: hidden;
    background: var(--backdrop);
    font-family: "Open Sans", Arial, sans-serif;
  }
  .stage {
    width: 1200px; height: 900px;
    display: flex; align-items: center; justify-content: center; gap: 40px;
  }
  .card {
    position: relative;
    width: 540px; height: 309px;
    background: var(--card);
    border-radius: 3px;
    box-shadow: 0 10px 24px rgba(0,0,0,0.35);
  }
  .brand {
    position: absolute;
    display: flex; align-items: center; gap: 10px;
    font-weight: 700; color: var(--ink-brown);
    text-transform: uppercase; letter-spacing: 0.2px;
    white-space: nowrap;
  }
  .brand-mark { width: 14px; height: 14px; background: var(--green); flex: none; }

  /* Contact side */
  .card-contact .brand { left: 40px; top: 44px; font-size: 20px; }
  .contact-list {
    position: absolute; left: 40px; top: 118px;
    list-style: none; font-size: 11px; color: var(--ink-muted); line-height: 19px;
    white-space: nowrap;
  }
  .contact-list li { display: flex; align-items: center; gap: 7px; }
  .contact-list svg { width: 11px; height: 11px; flex: none; }
  .divider { position: absolute; width: 1px; background: var(--green-line); }
  .divider-a { left: 196px; top: 120px; height: 150px; }
  .divider-b { left: 404px; top: 120px; height: 150px; }
  .person { position: absolute; left: 214px; top: 122px; width: 178px; white-space: nowrap; }
  .person-name { font-size: 20px; font-weight: 700; color: var(--green); text-transform: uppercase; line-height: 1.2; }
  .person-line { font-size: 13px; color: var(--ink-body); line-height: 1.6; }
  .address {
    position: absolute; right: 24px; bottom: 30px;
    font-size: 13px; color: var(--ink-body); line-height: 1.45; text-align: right;
    font-style: normal; white-space: nowrap;
  }

  /* Front side */
  .card-front .brand { left: 0; right: 0; top: 118px; justify-content: center; font-size: 24px; }
  .front-web {
    position: absolute; left: 0; right: 0; top: 170px;
    text-align: center; font-size: 15px; color: var(--green);
  }
</style>
</head>
<body>
<main class="stage">
  <section class="card card-contact">
    <div class="brand"><span class="brand-mark"></span>Velmar Industrial Coatings Inc.</div>

    <ul class="contact-list">
      <li>
        <svg viewBox="0 0 12 12"><rect width="12" height="12" rx="2" fill="#2f8a3a"/><path d="M3.5 2.5h2l.6 2-1.2.8a5 5 0 0 0 1.8 1.8l.8-1.2 2 .6v2a1 1 0 0 1-1 1A6.5 6.5 0 0 1 2.5 3.5a1 1 0 0 1 1-1z" fill="#cdbfb7"/></svg>
        (360) 555-0142
      </li>
      <li>
        <svg viewBox="0 0 12 12"><rect width="12" height="12" rx="2" fill="#2f8a3a"/><rect x="3" y="2.5" width="6" height="3" fill="#cdbfb7"/><rect x="2" y="5.5" width="8" height="4" fill="#cdbfb7"/></svg>
        (360) 555-0187
      </li>
      <li>
        <svg viewBox="0 0 12 12"><rect width="12" height="12" rx="2" fill="#2f8a3a"/><rect x="4" y="2" width="4" height="8" rx="1" fill="#cdbfb7"/></svg>
        (360) 555-0193
      </li>
      <li>
        <svg viewBox="0 0 12 12"><rect width="12" height="12" rx="2" fill="#2f8a3a"/><rect x="2" y="3.5" width="8" height="5" fill="#cdbfb7"/><path d="M2 3.5l4 3 4-3" stroke="#2f8a3a" stroke-width="0.8" fill="none"/></svg>
        reid@velmarfloors.com
      </li>
    </ul>

    <div class="divider divider-a"></div>

    <div class="person">
      <p class="person-name">Reid Calloway</p>
      <p class="person-line">1-800-555-0164</p>
      <p class="person-line">www.velmarfloors.com</p>
    </div>

    <div class="divider divider-b"></div>

    <address class="address">
      Velmar Inc.<br>
      PO Box 412<br>
      Harlow, WA 98577
    </address>
  </section>

  <section class="card card-front">
    <div class="brand"><span class="brand-mark"></span>Velmar Industrial Coatings Inc.</div>
    <p class="front-web">www.velmarfloors.com</p>
  </section>
</main>
</body>
</html>
```